Tobias Wrenfield - Cinematographer

NEED:
I'm looking for a sleek, professional, modern business card that will give give the recipient the impression that they can trust their production will go smoothly by hiring me. I will bring creativity and knowledge to their shoot, so that we can create powerful images.
I am looking for a card with a strong style and design ethos that could be expanded to a website and a full visual/graphic/design entity for me.
ABOUT ME:
I am a mid-twenties cinematographer, I work on music video, narrative short, commercial, and corporate projects. I blend the science and artistry of cameras and filmmaking to tell a story. I'm an artist, a technician, and a manager.
DESIGN:
I like sleek, simple design. Black, dark grays, white, dark navy, steel blues, I love cyan, but also cyan and red. I am not a fan of earthy tones. I generally prefer modern, san-serif fonts over serifs. My old logo was based on an aperture, a multi-blade device at the back of a lens that controls how much light passes through, but I made it with so many colors, that it doesn't necessarily lend itself to a specific color-scheme or design ethos. I liked that the aperture design provided a sense of the technical requirements of my job. I'm a fan of matte business cards, but am open to plenty of specialty print processes to make an outstanding card.
ATTACHED FILES:
My Old Rainbox Aperture Logo, plus a few designs I've tried playing around with, but am not tied to. I AM OPEN TO NEW DESIGNS, DO NOT FEEL TIED TO THIS.
**I've pulled my old logo down from the attached files, and instead attached other business cards I like, so as not to mislead you where I would like to go.
INFO:
Name: Tobias Wrenfield
Job: Cinematographer
Email: tkwrenfield@quillbox.example
Phone: 503.618.2907
Website: tobiaswrenfield.example
Updates
I'm adding some images of other cards that I like, and removing my old logo, since I'm looking for something new, and don't want that old logo to push anyone a certain direction.

```html
<!DOCTYPE html>
<html lang="en">
<head>
<meta charset="utf-8">
<title>Tobias Wrenfield – Cinematographer Business Card</title>
<link href="https://fonts.googleapis.com/css2?family=Montserrat:wght@300;400;700;800&display=swap" rel="stylesheet">
<style>
  :root {
    --stage: #e4e2df;
    --navy-deep: #25253a;
    --navy-mid: #3a3d55;
    --navy-soft: #5a5f74;
    --coral: #e8665e;
    --coral-text: #ef5a52;
    --ink: #1b1b1d;
    --white: #ffffff;
  }
  * { box-sizing: border-box; margin: 0; padding: 0; }
  html, body {
    width: 1200px; height: 747px; overflow: hidden;
    background: var(--stage);
    font-family: "Montserrat", Arial, sans-serif;
  }
  .stage {
    width: 1200px; height: 747px;
    display: flex; align-items: center; justify-content: center; gap: 60px;
  }
  .card {
    position: relative;
    width: 340px; height: 595px;
    overflow: hidden;
    box-shadow: 0 6px 18px rgba(0,0,0,.18);
  }

  /* Front */
  .card--front { background: var(--navy-deep); }
  .front__photo {
    position: absolute; inset: 0;
    background:
      radial-gradient(ellipse 70% 25% at 50% 60%, rgba(140,150,160,.45), transparent 70%),
      linear-gradient(180deg, var(--navy-deep) 0%, var(--navy-mid) 45%, var(--navy-soft) 65%, var(--navy-mid) 85%, var(--navy-deep) 100%);
  }
  .front__title {
    position: absolute; left: 40px; top: 168px; width: 270px;
  }
  .rule { display: block; height: 6px; }
  .rule--white { background: var(--white); width: 250px; margin-bottom: 6px; }
  .rule--coral { background: var(--coral-text); width: 240px; margin-top: 8px; }
  .name {
    color: var(--white);
    font-weight: 800; font-size: 44px; line-height: .95; letter-spacing: .5px;
  }
  .role {
    color: var(--coral-text);
    font-weight: 700; font-size: 38px; line-height: .95; margin-top: 4px;
  }

  /* Back */
  .card--back { background: var(--coral); }
  .contact {
    position: absolute; left: 28px; right: 22px; top: 220px;
    list-style: none;
  }
  .contact__item {
    position: relative;
    display: flex; align-items: center; gap: 12px;
    padding: 6px 0 6px;
    border-bottom: 2px solid var(--white);
  }
  .contact__item:first-child { border-top: 2px solid var(--white); margin-left: 18px; }
  .contact__icon {
    flex: 0 0 34px; width: 34px; height: 34px; border-radius: 50%;
    background: var(--ink);
    display: flex; align-items: center; justify-content: center;
  }
  .contact__label {
    display: block; color: var(--white);
    font-weight: 300; font-size: 15px; line-height: 1.1;
  }
  .contact__value {
    display: block; color: var(--ink);
    font-weight: 400; font-size: 14px; line-height: 1.2; letter-spacing: .3px;
  }
</style>
</head>
<body>
<main class="stage">
  <section class="card card--front" aria-label="Card front">
    <div class="front__photo" role="img" aria-label="Blurred night-time city lights in soft bokeh"></div>
    <div class="front__title">
      <span class="rule rule--white"></span>
      <h1 class="name">Tobias<br>Wrenfield</h1>
      <p class="role">Cinemat-<br>ographer</p>
      <span class="rule rule--coral"></span>
    </div>
  </section>

  <section class="card card--back" aria-label="Card back">
    <ul class="contact">
      <li class="contact__item">
        <span class="contact__icon">
          <svg width="16" height="20" viewBox="0 0 16 20" aria-hidden="true">
            <rect x="2" y="2" width="12" height="17" rx="2" fill="none" stroke="#fff" stroke-width="1.6"/>
            <rect x="4.5" y="4.5" width="7" height="5" fill="#fff"/>
            <line x1="11" y1="2" x2="11" y2="0" stroke="#fff" stroke-width="1.6"/>
          </svg>
        </span>
        <span><span class="contact__label">Mobile</span><span class="contact__value">503.618.2907</span></span>
      </li>
      <li class="contact__item">
        <span class="contact__icon">
          <svg width="20" height="14" viewBox="0 0 20 14" aria-hidden="true">
            <rect x="1" y="1" width="18" height="12" fill="none" stroke="#fff" stroke-width="1.6"/>
            <polyline points="1,1 10,8 19,1" fill="none" stroke="#fff" stroke-width="1.6"/>
          </svg>
        </span>
        <span><span class="contact__label">Email</span><span class="contact__value">tkwrenfield@quillbox.example</span></span>
      </li>
      <li class="contact__item">
        <span class="contact__icon">
          <svg width="20" height="20" viewBox="0 0 20 20" aria-hidden="true">
            <circle cx="10" cy="10" r="8" fill="none" stroke="#fff" stroke-width="1.6"/>
            <ellipse cx="10" cy="10" rx="3.5" ry="8" fill="none" stroke="#fff" stroke-width="1.4"/>
            <line x1="2" y1="10" x2="18" y2="10" stroke="#fff" stroke-width="1.4"/>
          </svg>
        </span>
        <span><span class="contact__label">Website</span><span class="contact__value">tobiaswrenfield.example</span></span>
      </li>
    </ul>
  </section>
</main>
</body>
</html>
```